Birthday, Anniversary, Engagement & Thank You cards

We need a foldover notecard design to send to our clients on special occasions (birthday, anniversary & engagements,) as well as a general thank you card. The design is to be the same on all cards, with the exception of the phrases "Happy Birthday," "Happy Anniversary," "Congrats on Your Engagement," and "Thank You."
Our logo needs to be on the card. Would like espresso background with orange lettering. Inside of card can be blank, as I will customize each file upon uploading to Quillmarch. Need modern, clean look with josefin font to match logo.

```html
<!DOCTYPE html>
<html lang="en">
<head>
<meta charset="utf-8">
<title>harlowe – Happy Birthday Notecard</title>
<link rel="stylesheet" href="https://fonts.googleapis.com/css2?family=Josefin+Sans:wght@300;400;600&family=Arimo:wght@400&display=swap">
<style>
  :root {
    --backdrop: #5f5866;
    --espresso: #2a1a13;
    --orange: #c86a2c;
    --paper: #ffffff;
    --ink: #2b211d;
    --ink-soft: #6a6260;
  }
  * { box-sizing: border-box; margin: 0; padding: 0; }
  html, body {
    width: 1200px;
    height: 900px;
    overflow: hidden;
  }
  body {
    background: var(--backdrop);
    position: relative;
  }
  .card {
    position: absolute;
    top: 300px;
    width: 520px;
    height: 298px;
    box-shadow: 4px 6px 10px rgba(0, 0, 0, 0.45);
    display: flex;
    flex-direction: column;
    align-items: center;
  }
  .card--front {
    left: 60px;
    background: var(--espresso);
    justify-content: center;
    color: var(--orange);
    font-family: "Josefin Sans", sans-serif;
    font-weight: 300;
    text-align: center;
  }
  .greeting__main {
    font-size: 66px;
    font-variant: small-caps;
    line-height: 1;
    letter-spacing: 1px;
  }
  .greeting__sub {
    font-size: 33px;
    font-variant: small-caps;
    line-height: 1;
    margin-top: 10px;
  }
  .card--back {
    left: 620px;
    background: var(--paper);
    padding-top: 118px;
    text-align: center;
  }
  .brand {
    display: flex;
    align-items: center;
    gap: 10px;
  }
  .brand__mark {
    width: 12px;
    height: 12px;
    background: var(--orange);
  }
  .brand__name {
    font-family: "Josefin Sans", sans-serif;
    font-weight: 600;
    font-size: 24px;
    line-height: 1;
    text-transform: uppercase;
    letter-spacing: 6px;
    color: var(--ink);
    padding-top: 3px;
  }
  .contact {
    font-family: "Arimo", sans-serif;
    font-size: 8.5px;
    line-height: 1.35;
    color: var(--ink-soft);
    margin-top: 20px;
    font-style: normal;
  }
  .contact__studio {
    display: block;
    font-size: 10px;
    color: var(--ink);
    margin-bottom: 4px;
  }
</style>
</head>
<body>
  <section class="card card--front" aria-label="Card front">
    <p class="greeting__main">Happy</p>
    <p class="greeting__sub">Birthday</p>
  </section>

  <section class="card card--back" aria-label="Card back">
    <div class="brand">
      <span class="brand__mark" aria-hidden="true"></span>
      <p class="brand__name">harlowe</p>
    </div>
    <address class="contact">
      <span class="contact__studio">Jewelry &amp; Design Studio</span>
      Birchgate Lane #7, Millstone<br>
      Plaza Easton, NH 03011<br>
      (555) 014-2290<br>
      info@harlowejewelry.com<br>
      www.harlowejewelry.com
    </address>
  </section>
</body>
</html>
```